Stationary package for modern new church start
Stationary for Bright Harbor Ministries
Stationary package for modern new church start  - Religion and Spirituality
Creative Brief
Professional
Daniel Mercer
Pastor
Bright Harbor Ministries P.O. Box 67890 Atlanta, GA 30318 The following P.O. Box is a generate one until I obtain one tomorrow. I will provide you with the correct P.O. Box sometime tomorrow or on Friday.
pastormercer@bhmx.org
www.bhmx.org
Please provide me with a complete stationary package that includes: Business Cards Letterhead Pen and pencil Email Signature USB Envelope Folder Fax Option Thank you Card front & Back Compliment Slip CD and CD Cover
Please include the following on the back: The Logo our our Ministry and our email address

```html
<!DOCTYPE html>
<html lang="en">
<head>
<meta charset="utf-8">
<title>Bright Harbor Ministries — Business Card</title>
<link rel="stylesheet" href="https://fonts.googleapis.com/css2?family=Montserrat:wght@500;700;800&family=Open+Sans:wght@400;600&display=swap">
<style>
  :root {
    --stage: #8e8e8e;
    --card: #ffffff;
    --card-shade: #f1f1f1;
    --brand-red: #e0141b;
    --brand-red-deep: #b80d12;
    --brand-blue: #2b8fd6;
    --ink: #4a4a4a;
    --ink-soft: #7a7a7a;
    --on-red: #ffffff;
  }
  * { margin: 0; padding: 0; box-sizing: border-box; }
  html, body { width: 1200px; height: 751px; overflow: hidden; }
  body {
    background: radial-gradient(ellipse at center, #a3a3a3 0%, var(--stage) 70%, #777 100%);
    font-family: "Open Sans", Arial, sans-serif;
    position: relative;
  }
  .card {
    position: absolute;
    top: 227px;
    width: 520px;
    height: 297px;
    background: linear-gradient(180deg, var(--card) 0%, var(--card-shade) 100%);
    box-shadow: 0 10px 28px rgba(0,0,0,0.28);
    overflow: hidden;
  }
  .card--front { left: 50px; }
  .card--back { left: 630px; }
  .card svg.shape { position: absolute; inset: 0; }

  .logo { position: absolute; display: flex; align-items: center; gap: 10px; }
  .logo__dot { width: 38px; height: 38px; border-radius: 50%; background: var(--brand-red); flex: none; }
  .logo__name {
    font-family: "Montserrat", Arial, sans-serif;
    font-weight: 800;
    color: var(--brand-red);
    line-height: 1.05;
    font-size: 20px;
  }
  .card--front .logo { left: 50%; top: 78px; transform: translateX(-50%); }
  .card--back .logo { left: 28px; top: 38px; }
  .card--back .logo__dot { width: 30px; height: 30px; }
  .card--back .logo__name { font-size: 15px; }

  .front__website {
    position: absolute;
    left: 0; right: 0; bottom: 36px;
    text-align: center;
    color: var(--on-red);
    font-family: "Montserrat", Arial, sans-serif;
    font-weight: 700;
    font-size: 17px;
    letter-spacing: 0.5px;
  }

  .person { position: absolute; left: 28px; top: 210px; }
  .person__name {
    font-family: "Montserrat", Arial, sans-serif;
    font-weight: 700;
    font-size: 17px;
    letter-spacing: 1px;
    color: var(--brand-red);
    text-transform: uppercase;
  }
  .person__title { font-size: 12px; color: var(--ink-soft); margin-top: 2px; }

  .contact {
    position: absolute;
    right: 26px; top: 62px;
    list-style: none;
    color: var(--on-red);
    font-size: 11px;
    line-height: 1;
  }
  .contact li { display: flex; align-items: center; justify-content: flex-end; gap: 8px; height: 23px; }
  .contact li.contact__address { height: auto; align-items: flex-start; margin-bottom: 8px; text-align: right; line-height: 1.45; }
  .contact svg { width: 12px; height: 12px; flex: none; fill: var(--on-red); }
</style>
</head>
<body>

  <section class="card card--front" aria-label="Business card front">
    <svg class="shape" viewBox="0 0 520 297" preserveAspectRatio="none" aria-hidden="true">
      <path d="M0 212 Q260 176 520 212 L520 297 L0 297 Z" fill="var(--brand-blue)"/>
      <path d="M0 218 Q260 182 520 218 L520 297 L0 297 Z" fill="var(--brand-red)"/>
      <path d="M0 226 Q260 196 520 226 L520 297 L0 297 Z" fill="var(--brand-red-deep)" opacity="0.35"/>
    </svg>
    <div class="logo">
      <span class="logo__dot"></span>
      <span class="logo__name">Bright Harbor<br>Ministries</span>
    </div>
    <p class="front__website">www.bhmx.org</p>
  </section>

  <section class="card card--back" aria-label="Business card back">
    <svg class="shape" viewBox="0 0 520 297" preserveAspectRatio="none" aria-hidden="true">
      <path d="M310 0 Q250 150 330 297" fill="none" stroke="var(--brand-blue)" stroke-width="4"/>
      <path d="M320 0 Q262 150 342 297 L520 297 L520 0 Z" fill="var(--brand-red)"/>
      <path d="M0 278 L60 278 L60 297 L0 297 Z" fill="var(--brand-blue)"/>
    </svg>

    <div class="logo">
      <span class="logo__dot"></span>
      <span class="logo__name">Bright Harbor<br>Ministries</span>
    </div>

    <div class="person">
      <p class="person__name">Daniel Mercer</p>
      <p class="person__title">Managing Director</p>
    </div>

    <ul class="contact">
      <li class="contact__address">
        <span>P.O. Box 67890<br>Atlanta, GA 30318</span>
        <svg viewBox="0 0 12 12"><path d="M6 0a4 4 0 0 0-4 4c0 3 4 8 4 8s4-5 4-8a4 4 0 0 0-4-4zm0 5.5A1.5 1.5 0 1 1 6 2.5a1.5 1.5 0 0 1 0 3z"/></svg>
      </li>
      <li><span>404 555 0182</span>
        <svg viewBox="0 0 12 12"><path d="M2.5 0.5l2 2.2-1.1 1.3c.7 1.6 2 2.9 3.6 3.6l1.3-1.1 2.2 2-1.2 2c-5 0-9.3-4.3-9.3-9.3z"/></svg></li>
      <li><span>404 555 0147</span>
        <svg viewBox="0 0 12 12"><rect x="1" y="4" width="10" height="6" rx="1"/><rect x="3" y="1" width="6" height="3"/></svg></li>
      <li><span>404 555 0193</span>
        <svg viewBox="0 0 12 12"><rect x="3" y="0.5" width="6" height="11" rx="1.2"/></svg></li>
      <li><span>pastormercer@bhmx.org</span>
        <svg viewBox="0 0 12 12"><path d="M0.5 2.5h11v7h-11z M0.5 2.5l5.5 4 5.5-4" fill="none" stroke="#fff" stroke-width="1.2"/></svg></li>
      <li><span>www.bhmx.org</span>
        <svg viewBox="0 0 12 12"><circle cx="6" cy="6" r="5" fill="none" stroke="#fff" stroke-width="1.2"/><path d="M1 6h10M6 1c-2.5 3-2.5 7 0 10M6 1c2.5 3 2.5 7 0 10" fill="none" stroke="#fff" stroke-width="1"/></svg></li>
    </ul>
  </section>

</body>
</html>
```